Halloway Crest Backers Guild business cards

Create a single-sided business card for the Halloway Crest Backers Guild based on the attached logo.
The additional data fields include Name, Title, Email, Phone, and website.
Please use the following as sample data:
Name: Dean Varrow
Title: Co-Founder / Investor
Email: deanvarrow@mailtern.net
Phone: 555-314-2706
Website: www.hcbackersguild.com

Target Market(s)

Start ups, entrepreneurs, venture capitalists

Industry/Entity Type

Investment

Contact Information for Business Card

Professional business card. Technology company.

Font styles to use
Serif
Sans Serif

Requirements
Must have
• Include the HCBG logo (attached)
• Name
• Title
• Email
• Phone
• Website
Should not have
• Cute, cartoony

```html
<!DOCTYPE html>
<html lang="en">
<head>
<meta charset="utf-8">
<title>Halloway Crest Backers Guild – Business Card</title>
<link href="https://fonts.googleapis.com/css2?family=Lato:wght@300;400;700;900&display=swap" rel="stylesheet">
<style>
  :root {
    --bg: #d9dcdb;
    --card: #f7f8f7;
    --band: #cfe6da;
    --green: #2e9e58;
    --ink: #4a4a4a;
    --ink-light: #9a9a9a;
  }
  html, body {
    margin: 0;
    width: 1200px;
    height: 1200px;
    overflow: hidden;
    background: var(--bg);
    font-family: "Lato", sans-serif;
  }
  .card {
    position: absolute;
    left: 100px;
    top: 314px;
    width: 1000px;
    height: 572px;
    background: var(--card);
    box-shadow: 0 6px 24px rgba(0,0,0,0.12);
    overflow: hidden;
  }
  .band { position: absolute; left: 0; width: 100%; background: var(--band); }
  .band--top { top: 0; height: 44px; }
  .band--bottom { bottom: 0; height: 66px; }
  .divider { position: absolute; background: var(--green); }
  .divider--vertical { left: 432px; top: 128px; width: 2px; height: 378px; }
  .divider--title { left: 470px; top: 252px; width: 330px; height: 2px; }
  .divider--contact { left: 520px; top: 430px; width: 340px; height: 2px; }

  .brand {
    position: absolute;
    left: 96px;
    top: 300px;
    display: flex;
    align-items: center;
    gap: 18px;
  }
  .brand__mark { width: 58px; height: 58px; border-radius: 50%; background: var(--green); }
  .brand__rule { width: 2px; height: 74px; background: var(--green); }
  .brand__name {
    font-weight: 400;
    font-size: 26px;
    line-height: 1.15;
    color: var(--green);
    width: 230px;
  }

  .person { position: absolute; left: 470px; top: 160px; }
  .person__name { font-size: 46px; letter-spacing: 1px; line-height: 1; color: var(--ink); }
  .person__first { font-weight: 900; }
  .person__last { font-weight: 300; color: var(--ink-light); }
  .person__title { font-size: 21px; font-weight: 400; color: var(--ink); margin-top: 6px; }

  .contacts { position: absolute; left: 490px; top: 278px; margin: 0; padding: 0; list-style: none; }
  .contacts__item {
    display: flex; align-items: center; gap: 14px;
    height: 44px; font-size: 22px; color: var(--ink);
  }
  .contacts__icon {
    width: 28px; height: 28px; border-radius: 50%;
    background: var(--green); color: #fff;
    font-size: 16px; display: flex; align-items: center; justify-content: center;
  }
</style>
</head>
<body>
  <div class="card">
    <div class="band band--top"></div>
    <div class="band band--bottom"></div>

    <div class="brand">
      <div class="brand__mark"></div>
      <div class="brand__rule"></div>
      <div class="brand__name">Halloway Crest Backers Guild</div>
    </div>

    <div class="divider divider--vertical"></div>

    <div class="person">
      <div class="person__name"><span class="person__first">DEAN</span> <span class="person__last">VARROW</span></div>
      <div class="person__title">Co-Founder / Investor</div>
    </div>
    <div class="divider divider--title"></div>

    <ul class="contacts">
      <li class="contacts__item"><span class="contacts__icon">p</span>555-314-2706</li>
      <li class="contacts__item"><span class="contacts__icon">e</span>deanvarrow@mailtern.net</li>
      <li class="contacts__item"><span class="contacts__icon">w</span>www.hcbackersguild.com</li>
    </ul>
    <div class="divider divider--contact"></div>
  </div>
</body>
</html>
```